Quilvane Folding Cyle helmet need launch designs and packaging

Quilvane makes the world's first fold flat cycle helmet. It's brilliant!
We have been developing the project for some time and are about to launch.
We want some great designs for our launch helmets, so that they have the widest possible appeal and so that people really want to own them. (It is only the graphics that need designing. The product design/shape is fixed now, as per the attached images.)
Our logo (attached, with more files available, on request) should be clearly seen on any design and on the packaging.
We would also like ideas regarding innovative packaging (don't forget that Quilvane folds flat) to reflect the high level of innovation in Quilvane as well as a simple carry bag that will be given away with Quilvane when one buys it. It is important that whatever is designed can be mass produced, very cost effectively. The packaging should help to make Quilvane stand out from the crowd by emphasizing what an amazing and thin product Quilvane is. The dimensions of a folded Quilvane helmet are roughly
Length 14.00 inches 355mm
Height 6.75 inches 171mm
Width 2.75 inches 70mm

We obviously want to communicate safety, convenience, innovation and just good old "I want one of those... now!"
Quilvane (www.quilvanehelmet.example) has already won Brisk Mechanics's Guardian Pioneer Prize of 2014 and had a successful crowdfunding campaign on Fundlark at the tail end of last year (www.fndl.example/at/quilvane).
The winning design(s) will be likely to be used for our launch and thus the designer will stand to gain a great deal of exposure.
This link will take you to the helmet page on Tredwicks and will show you many different current styles of helmets...http://www.tredwicks.example/cycling/accessories/helmets?discipline=Road&initMin=0&initMax=200 these may help you to understand what retailers believe the public want and should give you some inspiration.
Our pricing will be towards the most expensive end of the retail helmet market.
Updates

Thanks to everyone for the designs submitted so far. These have made me realise that the bag that I mention is being misunderstood. The carry bag that I am talking about is a bag that will be used to protect and carry the folded Quilvane helmet by the person that owns it, when it is not being worn.It should be innovative and may be a simple bag that will just hold and protect the or may be a bag that could hold books/phone/a small laptop as well? The choice is yours, as designers, but I want it to be durable and attractive. It could be a bag with a handle, with a tie string, with straps (like a ruck sack)... it could be nylon, canvas, material, neoprene etc...It is NOT a bag to carry the Quilvane home from the shops.I am going to try to get some 3d images of the Quilvane helmet as a couple of designers have asked me for these.If I can find something then I'll upload it. Added Wednesday, November 26, 2014

Reason: I am concerned that I haven't had as many designers submit a design as I would have liked in order to give this project the best chance.

Reason: I want to see if I can get some other designer to try and work on this... I have received some good stuff but nothing quite works well enough for me... yet... It may well still be that I award this to someone who has already committed work to this. And thank you very much to everyone that has, but I just want to see if there is anything out there that works better for me

Target Market(s)

All urban cyclists, male and female. Especially those prone to use a cycle scheme short term rental bike.

Industry/Entity Type

Safety

Font styles to use
Sans Serif

Requirements
Must have
• Helmet graphic design
• Packaging design
• A carrying bag accessory design, to protect and carry the helmet when it is closed
Nice to have
• Compelling reasons to buy.
• Innovative instruction ideas.
• Innovative swing ticket ideas
• Possibly also point of sale material ideas
Should not have
• Physical redesign of helmet

```html
<!DOCTYPE html>
<html lang="en">
<head>
<meta charset="utf-8">
<title>Quilvane carry bag – What's Missing?</title>
<link rel="stylesheet" href="https://fonts.googleapis.com/css2?family=Space+Grotesk:wght@500&display=swap">
<style>
  :root {
    --backdrop: #f1f1f3;
    --band-navy: #0a1c9c;
    --band-blue: #0a4d9e;
    --band-white: #ececee;
    --bike-blue: #1f5aa0;
    --type-white: #ffffff;
  }
  html, body {
    margin: 0;
    width: 1200px;
    height: 1200px;
    overflow: hidden;
    background: var(--backdrop);
  }
  .canvas {
    position: relative;
    width: 1200px;
    height: 1200px;
  }
  .bag-face {
    position: absolute;
    left: 165px;
    top: 50px;
    width: 870px;
    height: 1100px;
    display: flex;
  }
  .band { height: 100%; }
  .band--navy { width: 279px; background: var(--band-navy); }
  .band--blue { width: 259px; background: var(--band-blue); position: relative; }
  .band--white { width: 332px; background: var(--band-white); position: relative; }

  .slogan {
    position: absolute;
    left: 34px;
    bottom: 30px;
    margin: 0;
    writing-mode: vertical-rl;
    transform: rotate(180deg);
    font-family: "Space Grotesk", sans-serif;
    font-weight: 500;
    font-size: 94px;
    line-height: 84px;
    letter-spacing: 1px;
    color: var(--type-white);
    white-space: nowrap;
  }
  .slogan span { display: block; }

  .bike-graphic {
    position: absolute;
    left: 25px;
    top: 553px;
    width: 304px;
    height: 513px;
  }
</style>
</head>
<body>
  <main class="canvas">
    <section class="bag-face">
      <div class="band band--navy"></div>
      <div class="band band--blue">
        <h1 class="slogan"><span>WHAT'S</span><span>MISSING?</span></h1>
      </div>
      <div class="band band--white">
        <svg class="bike-graphic" viewBox="0 0 304 513" role="img" aria-label="Blue line illustration of a bicycle standing on end, missing its rider's helmet">
          <rect width="304" height="513" rx="6" fill="var(--bike-blue)" opacity="0.18"/>
        </svg>
      </div>
    </section>
  </main>
</body>
</html>
```